Zielgruppe
Wir sind ein Ingenieurbüro für Groß und Industriebauten. In diesem Flyer soll eine Dienstleistung, welche an unsere Kunden angeboten wird beworben werden. Unser Motto: persönlich professionell innovativ. Unser Unternehmen wird in diesem Jahr 30 Jahre alt, welches im Logo mit eingebaut ist. Bitte Das Logo Group als Hauptlogo nehmen und auch die Pantone 404 verwenden
Aufgabenstellung
Es soll eine Faltbroschüre werden - ein Beispiel eines Flyers lade ich mit Hoch. Das Logo ist in Pantone 404 und die Logos unserer Partnerunternehmen und Töchter hänge ich auch mit an und diese sollten als Firmenverbund berücksichtigt werden. Im Flyer 2 (2) sind die Informationen alle zusammengearbeitet

```html
<!DOCTYPE html>
<html lang="de">
<head>
<meta charset="utf-8">
<title>Faltbroschüre – Vom 3D Scan zum Gebäudemodell</title>
<link rel="stylesheet" href="https://fonts.googleapis.com/css2?family=Raleway:wght@400;500;600;700&display=swap">
<style>
  :root {
    --warm-grey: #7b756f;
    --band-grey: #8a8581;
    --band-light: #c9c6c3;
    --paper: #ffffff;
    --canvas: #efefef;
    --ink: #4a4a4a;
    --tick: #8a2f86;
    --on-grey: #ffffff;
  }
  * { box-sizing: border-box; margin: 0; padding: 0; }
  html, body { width: 1200px; height: 900px; overflow: hidden; }
  body {
    background: var(--canvas);
    font-family: "Raleway", sans-serif;
    color: var(--ink);
  }
  .spread {
    position: absolute; left: 30px; top: 30px;
    width: 1140px; height: 840px;
    background: var(--paper);
    box-shadow: 0 4px 18px rgba(0,0,0,.12);
    display: flex;
  }
  .panel { position: relative; width: 380px; height: 840px; }
  .panel--grey { background: var(--warm-grey); color: var(--on-grey); }

  .panel-title {
    position: absolute; left: 26px; top: 30px;
    font-size: 14px; font-weight: 500; letter-spacing: .02em;
    text-transform: uppercase;
  }
  .copy { font-size: 12px; line-height: 16px; }
  .ticks { list-style: none; font-size: 12px; line-height: 17px; }
  .ticks li { position: relative; padding-left: 16px; }
  .ticks li::before {
    content: "✓"; position: absolute; left: 0; top: 0;
    color: var(--tick); font-weight: 700;
  }

  .band { position: absolute; left: 0; top: 250px; width: 380px; height: 380px; }

  /* left panel */
  .references { position: absolute; left: 26px; top: 56px; width: 340px; }
  .needs-intro { position: absolute; left: 26px; top: 648px; width: 320px; }
  .needs { position: absolute; left: 26px; top: 695px; width: 330px; }
  .needs li { margin-bottom: 18px; }

  /* middle panel */
  .intro { position: absolute; left: 26px; top: 56px; width: 330px; }
  .step-num {
    position: absolute; width: 40px; height: 40px; border-radius: 50%;
    background: var(--paper); color: var(--warm-grey);
    font-size: 22px; font-weight: 700; font-style: italic;
    display: flex; align-items: center; justify-content: center;
  }
  .step-text { position: absolute; width: 280px; }
  .step-text strong { font-weight: 700; display: block; font-size: 13px; }

  .scan-object {
    position: absolute; left: 310px; top: 205px; width: 160px; height: 125px;
  }
  .cad-model { position: absolute; left: 230px; top: 690px; width: 110px; height: 85px; }

  /* right panel */
  .usage-intro { position: absolute; left: 26px; top: 56px; width: 330px; }
  .software { position: absolute; left: 80px; top: 125px; }
  .export-intro { position: absolute; left: 26px; top: 648px; width: 330px; }
  .formats { position: absolute; left: 80px; top: 700px; font-size: 11px; line-height: 15px; }
</style>
</head>
<body>
<main class="spread">

  <!-- Panel: Projektreferenzen -->
  <section class="panel panel--references">
    <h2 class="panel-title">Ein Auszug unserer Projektreferenzen</h2>
    <ul class="ticks references">
      <li>Neu- und Umbau / Sanierung von Produktions und Verwaltungsgebäuden</li>
      <li>Sanierung von Auffangtassen gem. WHG</li>
      <li>Neubau, Sanierung und Erweiterung von Abfüllflächen (VAwS)</li>
      <li>Erstellung von Brandschutzkonzepten</li>
      <li>Modifizierung der Löschwasserrückhaltung von Produktions- und Fertigungsgebäuden</li>
      <li>Abriss von Produktionsgebäuden einschl. Anlagenreinigung und Anlagenrückbau</li>
      <li>Betonsanierungsarbeiten</li>
    </ul>
    <svg class="band" viewBox="0 0 380 380">
      <defs>
        <linearGradient id="plantTones" x1="0" y1="0" x2="1" y2="1">
          <stop offset="0" stop-color="#6b5a4c"/>
          <stop offset=".45" stop-color="#8c7a6a"/>
          <stop offset=".7" stop-color="#5f7a5a"/>
          <stop offset="1" stop-color="#4a3c34"/>
        </linearGradient>
      </defs>
      <polygon points="0,0 380,110 380,372 0,380" fill="var(--band-grey)"/>
      <polygon points="0,345 380,325 380,352 0,372" fill="var(--band-light)"/>
      <g role="img" aria-label="Foto: Rohrleitungen und Stahlkonstruktion unter der Decke einer Industriehalle">
        <polygon points="0,50 380,130 380,325 0,345" fill="url(#plantTones)"/>
      </g>
    </svg>
    <p class="copy needs-intro">Für die Planung von neuen Anlagen im Bestand ein Kollisionsmodell benötigt wird.</p>
    <ul class="ticks needs copy">
      <li>Ein Aufmaß von schwer zugänglichen oder abgesperrten Bereichen benötigt wird.</li>
      <li>Eine Projektpräsentation durch ein anschauliches 3D Modell unterstützt werden soll.</li>
    </ul>
  </section>

  <!-- Panel: Ablauf -->
  <section class="panel panel--grey panel--process">
    <h2 class="panel-title">Vom 3D Scan zum Gebäudemodell</h2>
    <p class="copy intro">Mithilfe eines 3D Scans kann ein Originalgetreues Gebäudemodell eines Bestandsobjektes erstellt werden. Dabei können sämtliche, für die Planung relevanten Elemente und Störkanten in das Modell übertragen werden</p>

    <span class="step-num" style="left:62px; top:190px;">1.</span>
    <p class="copy step-text" style="left:125px; top:192px; width:230px;"><strong>Bestandsaufnahme</strong>Einzelne Objekte, Bereiche oder das gesamte Gebäude werden mit dem 3D Laserscanner aufgenommen</p>

    <span class="step-num" style="left:320px; top:335px;">2.</span>
    <p class="copy step-text" style="left:40px; top:330px; width:270px;">Die aufgenommenen Daten werden mit der Software Lumina Scan ausgewertet und verarbeitet.</p>

    <span class="step-num" style="left:62px; top:450px;">3.</span>
    <p class="copy step-text" style="left:115px; top:455px; width:240px;">Aus den verarbeiteten Daten wird eine Punktwolke erstellt.</p>

    <span class="step-num" style="left:320px; top:540px;">4.</span>
    <p class="copy step-text" style="left:40px; top:545px; width:270px;">Die Punktwolke wird in ein 3D fähiges CAD Programm (z.B. Bauform, PlanCAD) importiert.</p>

    <p class="copy step-text" style="left:40px; top:630px; width:270px;">Anhand der Punktwolke können die vorhandenen Bauteile im CAD Programm detailliert nachmodelliert werden.</p>

    <svg class="cad-model" viewBox="0 0 110 85" role="img" aria-label="Darstellung: modelliertes 3D Gebäudemodell in Grautönen">
      <defs>
        <linearGradient id="cadTones" x1="0" y1="0" x2="1" y2="1">
          <stop offset="0" stop-color="#d8d8d8"/>
          <stop offset="1" stop-color="#6d6d6d"/>
        </linearGradient>
      </defs>
      <polygon points="10,30 70,5 105,30 45,60" fill="url(#cadTones)"/>
      <polygon points="10,30 45,60 45,85 10,58" fill="#9a9a9a"/>
      <polygon points="45,60 105,30 105,55 45,85" fill="#5f5f5f"/>
    </svg>
  </section>

  <!-- Panel: Einsatz -->
  <section class="panel panel--usage">
    <h2 class="panel-title">Vielseitig einsetzbar</h2>
    <p class="copy usage-intro">Die erstellte Punktwolke kann in vielen CAD und Visualisierungsprogrammen weiterverarbeitet oder betrachtet werden.</p>
    <ul class="ticks software" style="font-size:11px; line-height:15px;">
      <li>Punktwerk Cap</li>
      <li>Modellwerk Viewer / Manage</li>
      <li>PlanCAD</li>
      <li>Bauform</li>
      <li>Formwerk 3D</li>
      <li>Rasterstudio</li>
    </ul>
    <svg class="band" viewBox="0 0 380 380">
      <defs>
        <linearGradient id="bridgeTones" x1="0" y1="0" x2="1" y2="1">
          <stop offset="0" stop-color="#dfe0dc"/>
          <stop offset=".4" stop-color="#a99880"/>
          <stop offset=".7" stop-color="#6e6657"/>
          <stop offset="1" stop-color="#8f8a6e"/>
        </linearGradient>
      </defs>
      <polygon points="0,75 380,0 380,380 0,372" fill="var(--band-grey)"/>
      <polygon points="0,340 380,345 380,372 0,362" fill="var(--band-light)"/>
      <g role="img" aria-label="Foto: steinerne Bogenbrücke mit Pfeilern im Fluss">
        <polygon points="0,125 380,40 380,345 0,340" fill="url(#bridgeTones)"/>
      </g>
    </svg>
    <p class="copy export-intro">Gängige Exportformate, die aus LuminaScan erstellt werden können, sind z.B.</p>
    <ul class="ticks formats">
      <li>E57</li><li>DXF</li><li>POD</li><li>LAS</li><li>IGS</li><li>CPE</li><li>RCP</li>
    </ul>
  </section>

  <svg class="scan-object" viewBox="0 0 160 125" role="img" aria-label="Darstellung: eingescannte Punktwolke einer Industrieanlage">
    <defs>
      <linearGradient id="scanTones" x1="0" y1="0" x2="1" y2="1">
        <stop offset="0" stop-color="#b9ad86"/>
        <stop offset=".5" stop-color="#8f9a8c"/>
        <stop offset="1" stop-color="#5a5048"/>
      </linearGradient>
    </defs>
    <polygon points="8,45 95,5 155,40 70,90" fill="url(#scanTones)"/>
    <polygon points="8,45 70,90 70,122 10,78" fill="#7c6e58"/>
    <polygon points="70,90 155,40 152,75 70,122" fill="#5d564d"/>
  </svg>

</main>
</body>
</html>
```